Marco T. Velden Crested Bay sales specialist

I need a postcard for a mailer to a specific waterfront association, and I want to let them know I just sold THE most premier waterfront on that area, and if they are looking to sell, I am the professional they should call. The photo I uploaded I would like on the card because that is the home I sold. I would like the Phrase : Laurel du Lac Sold! some place on the card, as well as all of my contact info and name of our Real Estate Firm.

Here is the name of My Firm and my contact info:\

Brickell Real Estate
Marco T. Velden
Office 555-014-3962
Cell 555-017-2485
Email Marco@brickellrealestate.example

Industry/Entity Type

Real Estate

Font styles to use
Serif

```html
<!DOCTYPE html>
<html lang="en">
<head>
<meta charset="utf-8">
<title>Laurel du Lac Sold! — Brickell Real Estate</title>
<link rel="stylesheet" href="https://fonts.googleapis.com/css2?family=Noto+Serif:ital,wght@0,400;0,700;1,700&display=swap">
<style>
  :root {
    --ink-white: #ffffff;
    --ink-black: #000000;
    --band-olive: #3a391b;
    --intro-panel: rgba(104, 78, 72, 0.82);
    --photo-dark-1: #2e2e2e;
    --photo-dark-2: #141414;
    --photo-dark-3: #4a4a4a;
    --photo-green-1: #5f7a45;
    --photo-green-2: #8c9a7a;
    --photo-gravel: #c9c3b6;
  }
  * { margin: 0; padding: 0; box-sizing: border-box; }
  html, body {
    width: 1200px;
    height: 924px;
    overflow: hidden;
    background: var(--ink-white);
  }
  .postcard {
    position: relative;
    width: 1200px;
    height: 924px;
    overflow: hidden;
    font-family: "Noto Serif", Georgia, serif;
    color: var(--ink-white);
  }
  .backdrop-photo {
    position: absolute;
    left: 0; top: 0;
    width: 1200px; height: 784px;
    background:
      radial-gradient(ellipse 520px 300px at 860px 200px, var(--photo-dark-3), transparent 70%),
      linear-gradient(180deg, var(--photo-dark-1) 0%, var(--photo-dark-2) 100%);
  }
  .footer-band {
    position: absolute;
    left: 0; top: 784px;
    width: 1200px; height: 140px;
    background: var(--band-olive);
  }
  .intro-panel {
    position: absolute;
    left: 24px; top: 23px;
    width: 563px; height: 326px;
    background: var(--intro-panel);
    border: 3px solid var(--ink-white);
    padding: 18px 14px 0 16px;
    font-size: 28px;
    line-height: 42px;
    letter-spacing: -0.3px;
    white-space: nowrap;
  }
  .intro-panel .drop-cap {
    float: left;
    font-size: 92px;
    line-height: 74px;
    margin: 6px 6px 0 -2px;
  }
  .tagline {
    position: absolute;
    left: 16px; top: 583px;
    width: 596px;
    font-style: italic;
    font-weight: 700;
    font-size: 42px;
    line-height: 52px;
    text-align: center;
    white-space: nowrap;
  }
  .sold-banner {
    position: absolute;
    left: 635px; top: 429px;
    width: 536px; height: 70px;
    background: var(--ink-black);
    border: 3px solid var(--ink-white);
    font-weight: 700;
    font-size: 45px;
    line-height: 62px;
    text-align: center;
    white-space: nowrap;
  }
  .sold-photo {
    position: absolute;
    left: 636px; top: 499px;
    width: 534px; height: 399px;
    border: 5px solid var(--ink-white);
    background:
      linear-gradient(180deg, #e9ece6 0%, var(--photo-green-2) 30%, var(--photo-green-1) 62%, var(--photo-gravel) 100%);
  }
  .agent-contact {
    position: absolute;
    left: 24px; top: 798px;
    width: 590px;
    font-size: 22px;
    line-height: 36px;
    white-space: nowrap;
  }
  .agent-contact .agent-name {
    font-weight: 700;
    font-size: 26px;
  }
</style>
</head>
<body>
  <main class="postcard">
    <div class="backdrop-photo" role="img" aria-label="Dimmed black-and-white photo of the lakeside cottage among tall pines"></div>
    <div class="footer-band"></div>

    <section class="intro-panel">
      <p><span class="drop-cap">B</span>rickell Real Estate has been<br>serving the real estate<br>needs of people in and around<br>the Athens, Ohio area since<br>1955. In fact, we are proud to<br>be the oldest active Real Estate<br>brokerage in Athens.</p>
    </section>

    <p class="tagline">“Let the PROFESSIONAL<br>handle your property”</p>

    <h1 class="sold-banner">Laurel du Lac Sold!</h1>
    <div class="sold-photo" role="img" aria-label="Colour photo of the sold white cottage surrounded by pines, garden beds and a gravel drive"></div>

    <address class="agent-contact" style="font-style: normal;">
      <p><span class="agent-name">Marco T. Velden</span> · Brickell Real Estate</p>
      <p>Office 555-014-3962 · Cell 555-017-2485</p>
      <p>Marco@brickellrealestate.example</p>
    </address>
  </main>
</body>
</html>
```